Webshop for baby shoes need new design

We are an innovative company selling a one of a kind product on a market with tough competition. We are looking to step up our business and need a new design for our shop.

We are looking for recognition as well as originality. The customer must immediately be able to identify navigation, shopping cart, buy buttons etc. We want warm welcoming colors, but not too strong as to not draw attention away from the products. Retro might be interesting, if "done right".

Suggested color palette: http://huepickerlab.example/#7r2kQmVx9a0b1

We have a logo (attached), but if you have a better idea we might go for that instead. Also, a couple of product images are attached for you to use in the design.

What we do NOT want is a shop that looks like a free template (tradeCart etc). Also, while we are selling baby shoes, we don't want to use the very worn our baby pink/blue scheme, so stay clear of this, thanks.

We suggest that you use this palette, or similar: http://huepickerlab.example/#7r2kQmVx9a0b1

Reason: We feel that we are getting closer to finding a design that we like, but there is still a bit to go. Also we want to give the chance to any late starters to show their idea. The competition is still open.

Target Market(s)

babies and their parents

Industry/Entity Type

Shopping

Requirements
Must have
• The usual webshop elements
- shopping cart
- product listing
- product page
- buy buttons
Nice to have
• - large footer area for links, info and function (see vimlo.example for an example)
- some kind of product navigation/filter (left, top or right)
- place for promotion banners

```html
<!DOCTYPE html>
<html lang="en">
<head>
<meta charset="utf-8">
<title>Toddlestep – Baby Shoes</title>
<link href="https://fonts.googleapis.com/css2?family=Coustard:wght@900&family=Yanone+Kaffeesatz:wght@400;500&family=Nothing+You+Could+Do&family=Open+Sans:wght@400;600;700&display=swap" rel="stylesheet">
<style>
:root{
  --teal:#12898c;
  --teal-dark:#0b6d70;
  --teal-light:#2fb3b3;
  --paper:#efe9d9;
  --paper-dark:#d9cfb8;
  --bg:#eae3cf;
  --ink:#3a3a36;
  --muted:#5b5a52;
  --olive:#7a6a3a;
  --red:#d21010;
  --gold:#f2c53c;
  --icon:#3f3f3b;
}
*{margin:0;padding:0;box-sizing:border-box}
html,body{width:988px;height:1200px;overflow:hidden}
body{position:relative;background:var(--bg);font-family:Arial,Helvetica,sans-serif;color:var(--ink)}
.side-art{position:absolute;top:0;width:142px;height:1200px}
.side-art.left{left:0;background:linear-gradient(180deg,rgba(234,227,207,0) 0%,rgba(234,227,207,0) 38%,var(--bg) 58%),linear-gradient(90deg,#e9e3d2 0%,#8a4a2a 30%,#b9d5e6 70%,#3c78b4 100%)}
.side-art.right{right:0;background:linear-gradient(180deg,rgba(234,227,207,0) 0%,rgba(234,227,207,0) 38%,var(--bg) 58%),linear-gradient(90deg,#3c78b4 0%,#b9d5e6 30%,#2f7f3a 70%,#e9e3d2 100%)}
.page{position:absolute;left:142px;top:0;width:704px;height:1200px;background:var(--paper);box-shadow:0 0 6px rgba(0,0,0,.25)}
.abs{position:absolute}

/* header */
.logo{left:16px;top:14px;display:flex;align-items:center;gap:10px}
.logo-mark{width:58px;height:58px;background:var(--teal);border-radius:8px}
.logo-name{font-family:'Coustard',serif;font-weight:900;font-size:40px;color:var(--teal)}
.claim{left:396px;top:12px;font-family:'Nothing You Could Do',cursive;font-size:13px;color:#555;white-space:nowrap}
.helpline{left:542px;top:15px;display:flex;gap:8px;align-items:center}
.helpline-text{font-family:'Open Sans',sans-serif;line-height:16px}
.helpline-title{color:var(--teal);font-size:14px;font-weight:600}
.helpline-num{color:#222;font-size:13px;font-weight:600}
.basket{left:432px;top:62px;width:272px;height:34px;background:var(--teal);clip-path:polygon(36px 0,100% 0,100% 100%,0 100%);color:#fff;font-style:italic;font-size:8.5px;line-height:13px;padding:4px 0 0 62px}
.basket svg{position:absolute;right:14px;top:4px}

/* nav */
.nav{left:0;top:96px;width:704px;height:28px;background:var(--teal);display:flex;align-items:center}
.nav a{position:absolute;top:0;height:28px;line-height:28px;color:#fff;font-size:9px;text-decoration:none;text-transform:uppercase}
.nav a.current{background:var(--teal-dark);padding:0 9px;left:0}
.search{position:absolute;left:586px;top:5px;width:110px;height:17px;background:#0d7a7d;border-radius:3px;color:#8fcfd0;font-size:8px;line-height:17px;padding-left:4px}
.search i{position:absolute;right:1px;top:0;width:17px;height:17px;border-radius:50%;background:#cfeeee}

/* hero */
.hero-title{left:15px;top:154px;font-family:'Coustard',serif;font-weight:900;font-size:21px;line-height:34px;color:#4a4a44;width:420px;letter-spacing:-.2px}
.hero-title span{color:var(--teal)}
.hero-product{left:6px;top:232px;width:332px;height:180px;border-radius:40% 50% 20% 20%;background:radial-gradient(ellipse at 50% 40%,#2c5e7c,#173c52 65%,#e9e4da 66%)}
.price{left:272px;top:238px;width:92px;height:92px;border-radius:50%;background:var(--gold);transform:rotate(12deg);text-align:center;color:#3a3020;box-shadow:0 2px 4px rgba(0,0,0,.2)}
.price b{display:block;font-family:'Open Sans',sans-serif;font-size:24px;margin-top:20px}
.price small{font-size:11px}
.dots{left:374px;top:408px;display:flex;gap:9px}
.dots i{width:13px;height:13px;border-radius:50%;background:#111}
.dots i:first-child{background:var(--teal-light)}
.categories{left:504px;top:138px;width:178px;height:266px;background:#f3eee1;box-shadow:0 1px 3px rgba(0,0,0,.2);padding:12px 0 0 22px}
.cat-head{font-family:'Open Sans',sans-serif;font-size:11px;font-weight:600;color:#222;margin-bottom:4px}
.cat-list{list-style:none;margin-bottom:9px}
.cat-list li{font-size:8.5px;line-height:15.6px;color:#333;padding-left:10px;position:relative}
.cat-list li:before,.links li:before{content:"";position:absolute;left:0;top:5px;border-left:4px solid var(--teal);border-top:3px solid transparent;border-bottom:3px solid transparent}
.btn{background:#eee8db;box-shadow:0 1px 3px rgba(0,0,0,.3);font-family:'Yanone Kaffeesatz',sans-serif;font-size:14px;color:#333;text-align:center;line-height:26px}
.btn em{font-style:normal;color:#c9962e;margin-left:6px}
.more{left:539px;top:390px;width:107px;height:26px}

/* reviews */
.reviews-band{left:0;top:440px;width:704px;height:328px;background:linear-gradient(180deg,#e8e1cd 0%,#e3dcc6 60%,#a9987a 100%);border-top:2px solid #d3c9b2}
.tag{left:12px;top:462px;width:118px;height:24px;background:var(--teal);color:#fff;font-family:'Open Sans',sans-serif;font-weight:700;font-size:11px;line-height:24px;text-align:center;box-shadow:2px 2px 0 #0a5f61}
.card{top:504px;width:161px;height:230px;background:#fbf9f3;box-shadow:0 0 3px rgba(0,0,0,.15)}
.card .shot{position:absolute;left:10px;top:10px;width:139px;height:86px;background:radial-gradient(ellipse at 50% 60%,var(--c),#fff 70%);box-shadow:0 1px 3px rgba(0,0,0,.2)}
.card h3{position:absolute;left:9px;top:108px;font-size:9.5px;color:var(--olive)}
.card p{position:absolute;left:9px;top:127px;width:143px;font-size:7.5px;line-height:12.7px;text-align:justify;color:#222}
.card .rrp{position:absolute;left:7px;top:192px;font-size:9.5px;font-style:italic;color:#111}
.card .save{position:absolute;right:8px;top:192px;font-size:9.5px;font-style:italic;color:var(--red)}
.card .btn{position:absolute;left:26px;top:214px;width:107px;height:26px}

/* friends */
.friends-title{left:26px;top:772px;font-family:'Nothing You Could Do',cursive;font-size:12px;color:#444}
.friend{width:200px;height:46px}
.friend .ico{position:absolute;left:0;top:0;width:32px;height:32px;border-radius:50%;background:var(--icon)}
.friend .ico svg{position:absolute;left:8px;top:8px}
.friend h4{position:absolute;left:45px;top:-12px;font-size:8px;color:#444;white-space:nowrap}
.friend p{position:absolute;left:45px;top:1px;width:150px;font-size:7.5px;line-height:13px;color:#555}

/* brands */
.rule{left:14px;width:676px;border-top:2px dashed #cfc6ae}
.brand{top:927px;font-family:'Open Sans',sans-serif;font-weight:700;font-size:13px;color:#222;transform:translateX(-50%);white-space:nowrap}

/* follow */
.follow-h{font-size:10px;font-weight:700;color:#444;letter-spacing:.3px}
.field{height:30px;background:#fff;border-radius:6px;box-shadow:inset 0 0 3px rgba(0,0,0,.2);font-size:8px;color:#333}
.like{position:absolute;left:10px;top:8px;display:flex;gap:6px;align-items:center;font-size:7px}
.like b{border:1px solid #aab;padding:1px 3px;background:#eef;font-weight:400;color:#335}
.subscribe{position:absolute;right:8px;top:6px;width:54px;height:19px;border-radius:10px;background:var(--teal);color:#fff;font-size:8.5px;text-align:center;line-height:19px}

/* footer */
.links{list-style:none;top:1068px}
.links li{position:relative;padding-left:9px;font-size:8.5px;font-style:italic;line-height:14px;color:#333}
.links li:before{border-left-color:#b5461c;top:4px}
.copyright{left:0;top:1176px;width:704px;text-align:center;font-size:8.5px;color:#222;border-top:1px solid #d6ccb5;padding-top:6px}
</style>
</head>
<body>
<div class="side-art left abs" role="img" aria-label="Brown leather baby shoe amid a splash of blue water"></div>
<div class="side-art right abs" role="img" aria-label="Green leather baby shoe amid a splash of blue water"></div>

<div class="page">
  <header>
    <div class="logo abs"><span class="logo-mark"></span><span class="logo-name">Toddlestep</span></div>
    <div class="claim abs">Start your claim now</div>
    <div class="helpline abs">
      <svg width="18" height="18" viewBox="0 0 24 24"><path fill="#12898c" d="M6.6 10.8a15 15 0 0 0 6.6 6.6l2.2-2.2c.3-.3.7-.4 1-.2 1.1.4 2.3.6 3.6.6.6 0 1 .4 1 1V20c0 .6-.4 1-1 1A17 17 0 0 1 3 4c0-.6.4-1 1-1h3.5c.6 0 1 .4 1 1 0 1.3.2 2.5.6 3.6.1.3 0 .7-.2 1z"/></svg>
      <div class="helpline-text"><div class="helpline-title">24 Hour Helpline</div><div class="helpline-num">0800 555 0142</div></div>
    </div>
    <div class="basket abs">Your Shopping Basket -<br>View Basket YouHave 0 items - Cost €0.00
      <svg width="34" height="26" viewBox="0 0 34 26" fill="none" stroke="#fff" stroke-width="2"><path d="M1 3h5l4 14h18l4-11H8"/><circle cx="13" cy="22" r="2"/><circle cx="25" cy="22" r="2"/></svg>
    </div>
  </header>

  <nav class="nav abs">
    <a class="current" href="#">Home</a>
    <a href="#" style="left:51px">Latest Articles</a>
    <a href="#" style="left:141px">Fearured Articles</a>
    <a href="#" style="left:253px">Popular Posts</a>
    <a href="#" style="left:346px">Authors</a>
    <a href="#" style="left:414px">Ecokite</a>
    <a href="#" style="left:479px">HD Video</a>
    <div class="search">Search<i></i></div>
  </nav>

  <section class="hero">
    <h1 class="hero-title abs"><span>Go to work</span> With the shoes That works for you</h1>
    <div class="hero-product abs" role="img" aria-label="Blue leather baby shoe with velcro strap"></div>
    <div class="price abs"><b>£18.99</b><small>PER PACK</small></div>
    <div class="dots abs"><i></i><i></i><i></i><i></i><i></i></div>
    <aside class="categories abs">
      <div class="cat-head">Women</div>
      <ul class="cat-list"><li>Ankle Boots</li><li>Heels</li><li>Trainers</li><li>Jackets</li><li>Jumpers &amp; Cardigans</li><li>Jeans</li><li>Bags &amp; Accessories</li></ul>
      <div class="cat-head">Men</div>
      <ul class="cat-list"><li>Trainers</li><li>Boots</li><li>Brogues &amp; Lace-Ups</li><li>Jackets</li></ul>
    </aside>
    <div class="more btn abs">More Catigories<em>»</em></div>
  </section>

  <section>
    <div class="reviews-band abs"></div>
    <div class="tag abs">Latest Reviews</div>
    <article class="card abs" style="left:7px"><div class="shot" style="--c:#2a3d6a" role="img" aria-label="Navy and orange baby boot"></div><h3>Lorem Ipsum is simply</h3><p>Text of the printing and typesetting industry. Lorem Ipsum has been the industry's standard dummy text ever since the 1500s,</p><span class="rrp">RRP: €88.51</span><span class="save">save €36.01</span><div class="btn">Add To Basket<em>»</em></div></article>
    <article class="card abs" style="left:184px"><div class="shot" style="--c:#e6e2d2" role="img" aria-label="White leather baby shoe"></div><h3>Lorem Ipsum is simply</h3><p>Text of the printing and typesetting industry. Lorem Ipsum has been the industry's standard dummy text ever since the 1500s,</p><span class="rrp">RRP: €88.51</span><span class="save">save €36.01</span><div class="btn">Add To Basket<em>»</em></div></article>
    <article class="card abs" style="left:362px"><div class="shot" style="--c:#3a66a8" role="img" aria-label="Blue lace-up baby shoe"></div><h3>Lorem Ipsum is simply</h3><p>Text of the printing and typesetting industry. Lorem Ipsum has been the industry's standard dummy text ever since the 1500s,</p><span class="rrp">RRP: €88.51</span><span class="save">save €36.01</span><div class="btn">Add To Basket<em>»</em></div></article>
    <article class="card abs" style="left:540px"><div class="shot" style="--c:#e6e2d2" role="img" aria-label="White leather baby shoe"></div><h3>Lorem Ipsum is simply</h3><p>Text of the printing and typesetting industry. Lorem Ipsum has been the industry's standard dummy text ever since the 1500s,</p><span class="rrp">RRP: €88.51</span><span class="save">save €36.01</span><div class="btn">Add To Basket<em>»</em></div></article>
  </section>

  <section>
    <div class="friends-title abs">Friends &amp; Recommendations</div>
    <div class="friend abs" style="left:23px;top:822px"><span class="ico"><svg width="16" height="16" viewBox="0 0 16 16"><path d="M2 8l6-6h6v6l-6 6z" fill="#fff"/><circle cx="11" cy="5" r="1.3" fill="#3f3f3b"/></svg></span><h4>When an unknown printer took</h4><p>Agalley of type and scrambled it to make a type specimen book.</p></div>
    <div class="friend abs" style="left:270px;top:823px"><span class="ico"><svg width="16" height="16" viewBox="0 0 16 16"><circle cx="8" cy="8" r="7" fill="#fff"/><path d="M4 5c2 0 3 2 2 4s2 3 3 5M9 2c0 2 2 3 5 3" stroke="#3f3f3b" stroke-width="1.5" fill="none"/></svg></span><h4>When an unknown printer took</h4><p>Agalley of type and scrambled it to make a type specimen book.</p></div>
    <div class="friend abs" style="left:503px;top:823px"><span class="ico"><svg width="16" height="16" viewBox="0 0 16 16"><ellipse cx="7" cy="7" rx="7" ry="5" fill="#fff"/><path d="M3 10l-2 4 5-3z" fill="#fff"/></svg></span><h4>When an unknown printer took</h4><p>Agalley of type and scrambled it to make a type specimen book.</p></div>
    <div class="friend abs" style="left:23px;top:876px"><span class="ico"><svg width="16" height="16" viewBox="0 0 16 16"><path d="M3 3h8l-3 3 6 6-2 2-6-6-3 3z" fill="#fff"/></svg></span><h4>When an unknown printer took</h4><p>Agalley of type and scrambled it to make a type specimen book.</p></div>
    <div class="friend abs" style="left:270px;top:877px"><span class="ico"><svg width="16" height="16" viewBox="0 0 16 16"><rect x="1" y="3" width="14" height="11" rx="1" fill="#fff"/><circle cx="5" cy="8" r="2" fill="#3f3f3b"/><path d="M9 7h4M9 10h4" stroke="#3f3f3b"/></svg></span><h4>When an unknown printer took</h4><p>Agalley of type and scrambled it to make a type specimen book.</p></div>
    <div class="friend abs" style="left:503px;top:877px"><span class="ico"><svg width="16" height="16" viewBox="0 0 16 16" fill="none" stroke="#fff" stroke-width="2"><path d="M3 7a5 5 0 0 1 9-2M13 9a5 5 0 0 1-9 2"/><path d="M12 1v4H8M4 15v-4h4"/></svg></span><h4>When an unknown printer took</h4><p>Agalley of type and scrambled it to make a type specimen book.</p></div>
  </section>

  <section>
    <div class="rule abs" style="top:912px"></div>
    <span class="brand abs" style="left:76px">Nine Paces</span>
    <span class="brand abs" style="left:188px">Crosswalk</span>
    <span class="brand abs" style="left:302px">Meadowbud</span>
    <span class="brand abs" style="left:414px">Hillfold</span>
    <span class="brand abs" style="left:528px">Pinegrove</span>
    <span class="brand abs" style="left:641px">Wanderly</span>
    <div class="rule abs" style="top:970px"></div>
  </section>

  <section>
    <h2 class="follow-h abs" style="left:17px;top:991px">FOLLOW THE WEB ON FRIENDBOOK</h2>
    <div class="field abs" style="left:12px;top:1010px;width:298px"><div class="like"><b>Gilla</b><span>13 557 personer gillar detta.</span></div></div>
    <h2 class="follow-h abs" style="left:392px;top:988px">FOLLOW THE WEB ON FRIENDBOOK</h2>
    <div class="field abs" style="left:387px;top:1010px;width:299px"><span style="position:absolute;left:12px;top:10px">Subscribe Now</span><span class="subscribe">Subscribe</span></div>
  </section>

  <footer>
    <ul class="links abs" style="left:30px"><li>Free shipping</li><li>Free return</li><li>14 day right of return</li><li>Large selection</li><li>Accessible Customer Service</li><li>Pay by invoice</li></ul>
    <ul class="links abs" style="left:214px"><li>Women</li><li>Men's Shoes</li><li>Kids Shoes</li><li>Shoe</li><li>Footwear brands AZ</li></ul>
    <ul class="links abs" style="left:370px;top:1069px"><li>About Us</li><li>Safety</li><li>Terms and conditions</li><li>Shipping Terms</li><li>Become an affiliate</li></ul>
    <ul class="links abs" style="left:558px"><li>Free shipping</li><li>Free return</li><li>14 day right of return</li><li>Large selection</li><li>Accessible Customer Service</li><li>Pay by invoice</li></ul>
    <div class="copyright abs">© Copyright Toddlestep. / Returns and Exchanges / Privacy Policy / Contact</div>
  </footer>
</div>
</body>
</html>
```